Postcard flyers for text vouchers

Postcard flyer to drive people to text for local vouchers delivered straight to their mobile, alternatively they can check out the websites.
Double sided, full colour A6 size. 105mm x 148.5mm http://www.brintafold.com/supplying-artwork.html
Postcard will be available in high footfall areas must be eye catching and compelling, but keep message simple. Wording as attached, side one headline grabbing, side two in style of a tag cloud giving a flavour of vouchers/savings available in their local area.
Updates

Project Deadline Extended
Reason: Research has shown wider area for website required therefore by county [Kelmarsh Deals] rather than smaller regions. Focus on entertainment and shopping for flyer.

Target Market(s)

Target 18-55 year olds
Core 25-45???
male and female

Requirements
Must have
• Stand out

```html
<!DOCTYPE html>
<html lang="en">
<head>
<meta charset="utf-8">
<title>Voucher Postcard</title>
<link rel="stylesheet" href="https://fonts.googleapis.com/css2?family=Ubuntu:wght@700&display=swap">
<style>
  :root {
    --bg: #353537;
    --red: #cc3136;
    --ink: #e9e9e9;
    --cut: #ffffff;
  }
  html, body {
    margin: 0;
    padding: 0;
    width: 1200px;
    height: 863px;
    overflow: hidden;
    background: var(--bg);
  }
  .postcard {
    display: block;
    width: 1200px;
    height: 863px;
  }
  .cut-line {
    stroke: var(--cut);
    stroke-width: 2.6;
    stroke-dasharray: 4 3;
    fill: none;
  }
  .coupon { fill: var(--red); }
  .coupon-perforation {
    stroke: var(--cut);
    stroke-width: 1.6;
    stroke-dasharray: 3 2.5;
    fill: none;
  }
  .coupon-name,
  .tagline {
    font-family: "Ubuntu", "Trebuchet MS", sans-serif;
    font-weight: 700;
    fill: var(--ink);
  }
  .scissors-ring { fill: none; stroke: var(--cut); stroke-width: 5; }
  .scissors-blade { fill: var(--cut); }
</style>
</head>
<body>
<svg class="postcard" viewBox="0 0 904 650" xmlns="http://www.w3.org/2000/svg" role="img" aria-label="Local voucher websites postcard">
  <defs>
    <symbol id="scissors" viewBox="0 0 60 70">
      <circle class="scissors-ring" cx="16" cy="13" r="9"/>
      <circle class="scissors-ring" cx="44" cy="13" r="9"/>
      <path class="scissors-blade" d="M21 20 L28 23 L55 66 L48 69 Z"/>
      <path class="scissors-blade" d="M39 20 L32 23 L5 66 L12 69 Z"/>
    </symbol>
  </defs>

  <rect width="904" height="650" fill="var(--bg)"/>

  <g class="layout" transform="rotate(-10.2 148 165)">
    <g class="guides">
      <line class="cut-line" x1="-300" y1="90"  x2="1200" y2="90"/>
      <line class="cut-line" x1="-300" y1="165" x2="1200" y2="165"/>
      <line class="cut-line" x1="-300" y1="242" x2="1200" y2="242"/>
      <line class="cut-line" x1="-300" y1="318" x2="1200" y2="318"/>
      <line class="cut-line" x1="-300" y1="397" x2="1200" y2="397"/>
      <line class="cut-line" x1="-300" y1="478" x2="148"  y2="478"/>
      <line class="cut-line" x1="148" y1="-300" x2="148" y2="900"/>
      <line class="cut-line" x1="772" y1="-300" x2="772" y2="900"/>
    </g>

    <g class="coupon-group">
      <rect class="coupon" x="148" y="165" width="624" height="232"/>
      <rect class="coupon-perforation" x="152" y="169" width="616" height="224"/>
      <line class="coupon-perforation" x1="152" y1="242" x2="768" y2="242"/>
      <line class="coupon-perforation" x1="152" y1="318" x2="768" y2="318"/>
      <text class="coupon-name" x="178" y="226" font-size="54" textLength="505" lengthAdjust="spacingAndGlyphs">Ashcombe Vouchers</text>
      <text class="coupon-name" x="180" y="302" font-size="56" textLength="548" lengthAdjust="spacingAndGlyphs">Harrowby Vouchers</text>
      <text class="coupon-name" x="182" y="381" font-size="62" textLength="575" lengthAdjust="spacingAndGlyphs">Dunmere Vouchers</text>
    </g>

    <g class="tagline-group">
      <text class="tagline" x="300" y="539" font-size="56" textLength="400" lengthAdjust="spacingAndGlyphs">great savings</text>
      <text class="tagline" x="346" y="571" font-size="30" textLength="268" lengthAdjust="spacingAndGlyphs">all in one place</text>
    </g>
  </g>

  <g class="scissors-set">
    <use href="#scissors" width="80" height="94" transform="translate(84 22) rotate(-10 40 47)"/>
    <use href="#scissors" width="80" height="94" transform="translate(676 16) rotate(80 40 47)"/>
    <use href="#scissors" width="80" height="94" transform="translate(800 56) rotate(80 40 47)"/>
    <use href="#scissors" width="80" height="94" transform="translate(36 282) rotate(-100 40 47)"/>
    <use href="#scissors" width="80" height="94" transform="translate(800 408) rotate(170 40 47)"/>
    <use href="#scissors" width="80" height="94" transform="translate(186 488) rotate(170 40 47)"/>
  </g>
</svg>
</body>
</html>
```